Detox Poster Design Project

I am a naturopath that works in Melbourne. I require a poster that I can put up in my natural therapies clinic that is advertising a detox program that I am offering. The program runs for 3 or 6 weeks and is designed to help your liver, gut and kidney cleanse toxins more efficiently, leaving you feeling energised and healthy.

I would like to see designs that are fresh, organic, clear and contemporary to look at. I want to sell the idea of feeling good, wellbeing and vitality to the potential client. Colours I like include greens, greys and blues.

The final design should communicate health and happiness.

• Please include the photo of the woman in nature.Poster size will be A2 594mm by 420mm
• I have attached the design work for my business cards that you can use. It would be great if the colours and style are in keeping with the existing design work for my business. I have also attached an extra image (almond milk photo) just in case you could see a use for it.

Many thanks.
• No hippy, new age looking design.

```html
<!DOCTYPE html>
<html lang="en">
<head>
<meta charset="utf-8">
<title>Detox Program Poster</title>
<link rel="stylesheet" href="https://fonts.googleapis.com/css2?family=Bodoni+Moda:wght@400&family=Rokkitt:wght@300&display=swap">
<style>
  :root {
    --paper: #ffffff;
    --frame-line: #1b5fa8;
    --sky-top: #1a63b8;
    --sky-low: #5fb0e6;
    --sea-top: #1f7fc4;
    --sea-low: #63b3dc;
    --fabric-deep: rgba(18, 62, 160, 0.9);
    --fabric-mid: rgba(30, 88, 190, 0.7);
    --figure-light: rgba(240, 246, 250, 0.85);
    --figure-blue: rgba(30, 100, 200, 0.75);
    --ring: #8fd3ee;
    --cloud-edge: #d8f1fa;
    --text-blue: #2a9cc8;
    --accent-orange: #e8603c;
    --headline: #2fbde0;
    --divider: #b9dcea;
  }
  html, body {
    margin: 0;
    padding: 0;
    overflow: hidden;
    background: var(--paper);
  }
  .poster {
    position: relative;
    width: 1200px;
    height: 860px;
    background: var(--paper);
    overflow: hidden;
    font-family: "Rokkitt", Georgia, serif;
    font-weight: 300;
  }
  .poster__frame {
    position: absolute;
    left: 21px;
    top: 21px;
    width: 1154px;
    height: 812px;
    border: 1px solid var(--frame-line);
    box-sizing: border-box;
    overflow: hidden;
  }
  .hero-photo {
    position: absolute;
    inset: 0;
    background:
      linear-gradient(180deg,
        var(--sky-top) 0%,
        #2f7fcc 30%,
        var(--sky-low) 57%,
        var(--sea-top) 58%,
        #2d8fcc 75%,
        var(--sea-low) 100%);
  }
  .hero-photo__fabric {
    position: absolute;
    left: 20px;
    top: 10px;
    width: 990px;
    height: 310px;
    border-radius: 50%;
    transform: rotate(-3deg);
    background: radial-gradient(ellipse at 45% 45%,
      var(--fabric-deep) 0%,
      var(--fabric-mid) 45%,
      rgba(30, 88, 190, 0) 72%);
  }
  .hero-photo__figure {
    position: absolute;
    left: 790px;
    top: 120px;
    width: 300px;
    height: 520px;
    border-radius: 50%;
    background: radial-gradient(ellipse at 50% 40%,
      var(--figure-light) 0%,
      var(--figure-blue) 45%,
      rgba(30, 100, 200, 0) 72%);
  }
  .cloud {
    position: absolute;
    inset: 0;
    width: 100%;
    height: 100%;
  }
  .program-copy {
    position: absolute;
    left: 188px;
    top: 424px;
    width: 480px;
    text-align: center;
    color: var(--text-blue);
  }
  .program-copy__intro {
    margin: 0;
    font-size: 22px;
    line-height: 30px;
  }
  .divider {
    height: 0;
    border-top: 1px dotted var(--divider);
    margin: 44px 20px 0;
  }
  .divider--second {
    margin-top: 18px;
  }
  .practitioner {
    margin: 11px 0 0;
  }
  .practitioner__name {
    display: block;
    color: var(--accent-orange);
    font-size: 32px;
    line-height: 36px;
  }
  .practitioner__credentials {
    display: block;
    font-size: 20px;
    line-height: 28px;
  }
  .contact {
    margin: 12px 0 0;
  }
  .contact__phone {
    display: block;
    font-size: 40px;
    line-height: 46px;
    letter-spacing: 1px;
  }
  .contact__email {
    display: block;
    font-size: 19px;
    line-height: 24px;
  }
  .headline-block {
    position: absolute;
    left: 690px;
    top: 632px;
    width: 326px;
    text-align: center;
  }
  .headline-block__emblem {
    display: block;
    width: 48px;
    height: 48px;
    margin: 0 auto 26px;
    border-radius: 50%;
    background: var(--headline);
  }
  .headline-block__title {
    margin: 0;
    font-family: "Bodoni Moda", Georgia, serif;
    font-weight: 400;
    font-size: 72px;
    line-height: 72px;
    letter-spacing: 6px;
    color: var(--headline);
  }
</style>
</head>
<body>
  <main class="poster">
    <div class="poster__frame">
      <div class="hero-photo">
        <div class="hero-photo__fabric" role="img" aria-label="Photo area: long flowing blue silk scarf billowing across the sky"></div>
        <div class="hero-photo__figure" role="img" aria-label="Photo area: woman in white top and blue pants leaping above the sea, holding the scarf"></div>
      </div>
      <svg class="cloud" viewBox="0 0 1154 812" aria-hidden="true">
        <defs>
          <radialGradient id="cloud-fill" cx="40%" cy="70%" r="70%">
            <stop offset="0%" stop-color="#ffffff"/>
            <stop offset="70%" stop-color="#ffffff"/>
            <stop offset="100%" stop-color="#d8f1fa"/>
          </radialGradient>
        </defs>
        <g fill="#8fd3ee" opacity="0.3">
          <circle cx="394" cy="891" r="640"/>
          <circle cx="895" cy="838" r="350"/>
        </g>
        <g fill="#8fd3ee" opacity="0.45">
          <circle cx="394" cy="891" r="614"/>
          <circle cx="895" cy="838" r="324"/>
        </g>
        <g fill="url(#cloud-fill)">
          <circle cx="394" cy="891" r="590"/>
          <circle cx="895" cy="838" r="301"/>
        </g>
      </svg>
    </div>

    <section class="program-copy">
      <p class="program-copy__intro">The program runs for<br>3 or 6 weeks and is designed to help<br>your liver, gut and kidney cleanse<br>toxins more efficiently, leaving you<br>feeling energised and healthy.</p>
      <div class="divider"></div>
      <p class="practitioner">
        <span class="practitioner__name">Clara Wendell B.A. B.H.Sc.</span>
        <span class="practitioner__credentials">(Naturopathy) Member NTWA</span>
      </p>
      <div class="divider divider--second"></div>
      <p class="contact">
        <span class="contact__phone">T: 0400 318 742</span>
        <span class="contact__email">E: info@clarawendell.com.au</span>
      </p>
    </section>

    <section class="headline-block">
      <span class="headline-block__emblem" aria-hidden="true"></span>
      <h1 class="headline-block__title">DETOX</h1>
    </section>
  </main>
</body>
</html>
```